Brightway Inc. Business Card Design

Brightway Inc. is in search of a great clean design for our business cards!

Looking to incorporate our full logo and watermark on side one (however, I am open to having the text and watermark separated within the design.)

On side two, I am looking to have contact information (Name, Position, Phone #, Email, Website (www.thebrightway.ca). Can have the logo and/or watermark as part of the design if applicable.

Please add tagline "Where Shine Counts" on either side 1 or 2. This tagline can be in a sans serif, serif or cursive font as long as it compliments overall design. Capitalization can be title or sentence case depending on how it fits within the design.

Get creative!! Looking for a clean, crisp, premium design! Looking for a glossy card finish with spot UV features when printed. Cards will also be printed with rounded corners. Standard dimensions (3.5 x 2).

Target Market(s)

B2B - primary clients are business owners or property management corporations. (residential jobs are few and far between)

Industry/Entity Type

Business

Contact Information for Business Card

- clean, crisp design
- double sided
- spot UV accents and glossy finish upon printing
- standard business card size (3.5 x 2) with rounded corners
- please see project description for requirements per side

Font styles to use
Sans Serif

Requirements
Must have
• - adequate bleeds with print ready files
• - cohesive design elements between side 1 & 2
• - spot UV elements (can be on both sides or just one, use your discretion)
• - colour pallet should match the logo file provided
• - incorporate tagline "where shine counts" (this tagline can be in a serif or sans serif font as long as it is complimentary to the overall design.
Nice to have
• - Premium elements with a clean design
Should not have
• - Please omit cartoon or whimsical like designs, think premium.
• - Colours should not stray from the pallet of the provided logo.

```html
<!DOCTYPE html>
<html lang="en">
<head>
<meta charset="utf-8">
<title>Brightway Inc. Business Card</title>
<link href="https://fonts.googleapis.com/css2?family=Montserrat:wght@500;600;700&display=swap" rel="stylesheet">
<style>
  :root {
    --navy: #1d2562;
    --navy-light: #36447f;
    --teal: #1bb5b5;
    --teal-light: #3fd0cc;
    --white: #ffffff;
    --paper: #f1f1f1;
    --ink: #3a3a44;
    --backdrop: #2b2b2e;
  }
  * { margin: 0; padding: 0; box-sizing: border-box; }
  html, body { width: 1200px; height: 834px; overflow: hidden; }
  body {
    background: var(--backdrop);
    font-family: "Montserrat", sans-serif;
    display: flex;
    align-items: center;
    justify-content: space-between;
    padding: 0 40px;
  }
  .card {
    position: relative;
    width: 540px;
    height: 309px;
    border-radius: 12px;
    overflow: hidden;
    box-shadow: 0 14px 30px rgba(0,0,0,0.45);
  }
  .card-art { position: absolute; inset: 0; width: 100%; height: 100%; }
  .logo {
    position: absolute;
    display: flex;
    align-items: center;
    gap: 10px;
    font-weight: 700;
    letter-spacing: 0.5px;
  }
  .logo-mark { width: 30px; height: 30px; background: var(--teal); }
  .card-front .logo {
    left: 0; right: 0; top: 112px;
    justify-content: center;
    font-size: 38px;
    color: var(--teal-light);
  }
  .card-front .logo .logo-mark { width: 38px; height: 38px; background: var(--teal-light); }
  .tagline {
    position: absolute;
    right: 120px;
    bottom: 62px;
    font-size: 14px;
    font-weight: 600;
    color: var(--navy);
    transform: rotate(-14deg);
  }
  .card-back .logo {
    right: 70px; top: 48px;
    font-size: 28px;
    color: var(--navy);
  }
  .contact { position: absolute; left: 40px; top: 158px; color: var(--ink); }
  .contact-name { font-size: 17px; font-weight: 700; }
  .contact-role { font-size: 15px; font-weight: 500; color: var(--teal); margin-bottom: 10px; }
  .contact-line { display: flex; align-items: center; gap: 8px; font-size: 13px; font-weight: 500; margin-top: 5px; }
  .contact-line svg { width: 14px; height: 14px; stroke: var(--teal); fill: none; stroke-width: 1.6; }
  .website {
    position: absolute;
    right: 24px;
    bottom: 52px;
    font-size: 12px;
    font-weight: 500;
    color: var(--white);
    transform: rotate(-24deg);
  }
</style>
</head>
<body>

  <section class="card card-front">
    <svg class="card-art" viewBox="0 0 540 309" preserveAspectRatio="none" aria-hidden="true">
      <defs>
        <radialGradient id="navyGlow" cx="0.45" cy="0.45" r="0.7">
          <stop offset="0" stop-color="#4a5590"/>
          <stop offset="1" stop-color="#1d2562"/>
        </radialGradient>
      </defs>
      <rect width="540" height="309" fill="url(#navyGlow)"/>
      <path d="M0,232 C210,262 420,215 540,92 L540,309 L0,309 Z" fill="#ffffff"/>
      <path d="M0,242 C215,272 425,225 540,104 L540,309 L0,309 Z" fill="#1bb5b5"/>
    </svg>
    <div class="logo"><span class="logo-mark"></span>BRIGHTWAY INC.</div>
    <p class="tagline">Where Shine Counts</p>
  </section>

  <section class="card card-back">
    <svg class="card-art" viewBox="0 0 540 309" preserveAspectRatio="none" aria-hidden="true">
      <rect width="540" height="309" fill="#f4f4f4"/>
      <path d="M0,258 C230,300 440,250 540,118 L540,309 L0,309 Z" fill="#1d2562"/>
      <path d="M0,262 C232,304 442,256 540,126 L540,309 L0,309 Z" fill="#ffffff"/>
      <path d="M0,270 C235,312 445,266 540,138 L540,309 L0,309 Z" fill="#1bb5b5"/>
    </svg>
    <div class="logo"><span class="logo-mark"></span>BRIGHTWAY INC.</div>
    <div class="contact">
      <p class="contact-name">Alex Moreau</p>
      <p class="contact-role">President</p>
      <p class="contact-line">
        <svg viewBox="0 0 16 16"><path d="M3 2 L6 2 L7 5 L5 6.5 C6 8.5 7.5 10 9.5 11 L11 9 L14 10 L14 13 C14 13.8 13.3 14.3 12.5 14 C7 12.5 3.5 9 2 3.5 C1.8 2.7 2.3 2 3 2 Z"/></svg>
        555-010-2847
      </p>
      <p class="contact-line">
        <svg viewBox="0 0 16 16"><rect x="1.5" y="3.5" width="13" height="9"/><path d="M1.5 3.5 L8 9 L14.5 3.5"/></svg>
        info@thebrightway.ca
      </p>
    </div>
    <p class="website">www.thebrightway.ca</p>
  </section>

</body>
</html>
```